Realtor Business Card for Marisol!

I sell real estate in a tropical location near the ocean, beaches and palm trees.

The homes are higher end, luxury. I want a card that is professional and attention-grabbing. In a sea full of competition, I need to stand out! I don't want the run-of-the mill card that looks like everyone else's with a different name. I want people to say "wow!".
Updates

Project Deadline Extended Reason: I have a little more time that originally anticipated. Added Friday, July 7, 2017

Target Market(s)

All.

Industry/Entity Type

Real Estate Agent

Contact Information for Business Card

Name: Marisol Vankeer-Odham
Email: marisol@harborview-estates.example
Website: www.harborviewestates.example
Phone: 555.418.7263

Font styles to use
Serif

Colors

Designer to choose colors to be used in the design.

Requirements
Must have
• All attachments.
Nice to have
• Gold edges
• Transparent card
• Unique shape

```html
<!DOCTYPE html>
<html lang="en">
<head>
<meta charset="utf-8">
<title>Harborview Estates – Business Card</title>
<link rel="stylesheet" href="https://fonts.googleapis.com/css2?family=Open+Sans:wght@400&family=Permanent+Marker&display=swap">
<style>
  :root {
    --page: #ffffff;
    --card: #f2f2f1;
    --ink: #161616;
    --text: #2a2a2a;
    --violet: #8a5cc8;
    --violet-deep: #5b2a9a;
    --violet-mid: #9a6ad6;
    --haze: #c9c3d8;
    --sand: #d9c2b6;
  }
  * { box-sizing: border-box; margin: 0; padding: 0; }
  html, body {
    width: 1200px; height: 1200px; overflow: hidden;
    background: var(--page);
  }
  .sheet { position: relative; width: 1200px; height: 1200px; }
  .card {
    position: absolute; left: 162px; width: 876px; height: 448px;
    background: var(--card); overflow: hidden;
    box-shadow: 0 2px 10px rgba(0,0,0,0.18);
  }
  .card--front { top: 186px; }
  .card--back { top: 676px; }

  .coast-scene {
    position: absolute; left: 0; right: 0; top: 150px; bottom: 0;
    background:
      linear-gradient(180deg, rgba(242,242,241,1) 0%, rgba(201,195,216,0.7) 18%, rgba(120,90,120,0.85) 38%, var(--sand) 56%, var(--violet-mid) 62%, var(--violet) 78%, var(--violet-deep) 100%);
  }
  .wordmark {
    position: absolute; left: 40px; top: 30px;
    font-family: "Open Sans", sans-serif; font-weight: 400;
    font-size: 88px; line-height: 1; letter-spacing: 1px; color: var(--ink);
  }
  .wordmark-sub {
    position: absolute; left: 200px; top: 122px;
    font-family: "Permanent Marker", cursive;
    font-size: 46px; line-height: 1; letter-spacing: 2px; color: var(--ink);
  }
  .brand-badge {
    position: absolute; left: 716px; top: 36px; width: 128px; height: 128px;
    border-radius: 50%; background: var(--violet);
    display: flex; align-items: center; justify-content: center;
    font-family: "Open Sans", sans-serif; font-weight: 400;
    font-size: 17px; color: #ffffff; letter-spacing: 0.5px;
  }

  .contact {
    position: absolute; left: 41px; top: 42px;
    font-family: "Open Sans", sans-serif; font-size: 22px; line-height: 30px;
    color: var(--text); list-style: none;
  }
  .portrait {
    position: absolute; left: 717px; top: 23px; width: 126px; height: 126px;
    border-radius: 50%;
    background: radial-gradient(circle at 50% 40%, #8a8a8a 0%, #4a4a4a 60%, #2a2a2a 100%);
  }
  .shore-band {
    position: absolute; left: 0; right: 0; bottom: 0; height: 110px;
    background: linear-gradient(180deg, var(--sand) 0%, var(--violet-mid) 12%, var(--violet) 55%, var(--violet-deep) 100%);
  }
</style>
</head>
<body>
<main class="sheet">
  <section class="card card--front">
    <div class="coast-scene" role="img" aria-label="Photo of a palm-lined coastal neighbourhood above a beach, tinted violet"></div>
    <h1 class="wordmark">HARBORVIEW</h1>
    <p class="wordmark-sub">ESTATES</p>
    <div class="brand-badge">Harborview</div>
  </section>

  <section class="card card--back">
    <ul class="contact">
      <li>Name: Marisol Vankeer-Odham</li>
      <li>Email: marisol@harborview-estates.example</li>
      <li>Website: www.harborviewestates.example</li>
      <li>Phone: (555)418-7263</li>
    </ul>
    <div class="portrait" role="img" aria-label="Black and white portrait photo of the agent"></div>
    <div class="shore-band" role="img" aria-label="Photo strip of violet-tinted shoreline and water"></div>
  </section>
</main>
</body>
</html>
```